Marisol transparent business card

I would like to have a transparent business card created.
A simple yet classy card with
Website www.MarisolPennington.example
Phone # 555-214-7396
I would like my full photo on the card as well as my logo.

Target Market(s)

The business card will be printed on transparent card stock.
Www.MarisolPennington.example
Phone 555-214-7396
I would like my pic on the card and my logo
Author, Speaker, & Wealth architect

Industry/Entity Type

Business

Contact Information for Business Card

Www.MarisolPennington.example
Phone 555-214-7396

Font styles to use
Serif
Decorative
Script

Requirements
Must have
• The business card will be printed on transparent card stock.
• Www.MarisolPennington.example
• Phone 555-214-7396
• I would like my pic on the card and my logo
• Author, Speaker, & Wealth architect
Nice to have
• If I could have the tattoo on my pic blurred out or airbrushed over

```html
<!DOCTYPE html>
<html lang="en">
<head>
<meta charset="utf-8">
<title>Marisol Pennington Business Card</title>
<link rel="stylesheet" href="https://fonts.googleapis.com/css2?family=Great+Vibes&family=Cormorant+Garamond:wght@500;600&family=Open+Sans:wght@400&display=swap">
<style>
  :root {
    --page-bg: #e9e6e2;
    --card-black: #0b0b0b;
    --card-edge: #1c1c1c;
    --gold: #d9a521;
    --gold-soft: #b98a18;
    --silver: #d7d7d7;
    --ink-light: #f2f2f2;
    --photo-top: #3a2a22;
    --photo-bottom: #121010;
  }
  * { box-sizing: border-box; margin: 0; padding: 0; }
  html, body {
    width: 1200px; height: 900px; overflow: hidden;
    background: var(--page-bg);
  }
  .canvas {
    position: relative; width: 1200px; height: 900px;
  }
  .card {
    position: absolute; top: 296px;
    width: 540px; height: 309px;
    background: var(--card-black);
    border: 1px solid var(--card-edge);
    box-shadow: 0 10px 28px rgba(0,0,0,.28);
    overflow: hidden;
  }
  .card--front { left: 45px; }
  .card--back { left: 615px; }

  .portrait {
    position: absolute; left: 22px; bottom: 0;
    width: 170px; height: 270px;
    border-radius: 60px 60px 0 0;
    background: linear-gradient(180deg, var(--photo-top), var(--photo-bottom));
  }

  .brand-mark {
    position: absolute; left: 250px; top: 30px;
    display: flex; align-items: center; gap: 8px;
  }
  .brand-mark__circle {
    width: 30px; height: 30px; border-radius: 50%;
    border: 2px solid var(--gold);
  }
  .brand-mark__name {
    font-family: "Cormorant Garamond", serif; font-weight: 600;
    font-size: 16px; color: var(--gold); letter-spacing: .5px;
  }

  .name {
    position: absolute; left: 228px; top: 76px;
    font-family: "Great Vibes", cursive; font-size: 40px; line-height: 1;
    white-space: nowrap;
  }
  .name__first { color: var(--gold); }
  .name__last { color: var(--ink-light); }

  .tagline {
    position: absolute; left: 262px; top: 122px;
    font-family: "Cormorant Garamond", serif; font-weight: 500;
    font-size: 10.5px; letter-spacing: .6px; color: var(--ink-light);
    text-transform: uppercase; white-space: nowrap;
  }

  .contact {
    position: absolute; left: 238px; top: 160px;
    font-family: "Open Sans", sans-serif; font-size: 14px;
    color: var(--ink-light); list-style: none;
  }
  .contact li { display: flex; align-items: center; gap: 8px; line-height: 22px; }
  .contact svg { width: 12px; height: 12px; fill: var(--gold); flex: none; }

  .roles {
    position: absolute; left: 238px; top: 222px;
    font-family: "Open Sans", sans-serif; font-size: 14.5px;
    color: var(--ink-light); white-space: nowrap;
  }

  .back-mark {
    position: absolute; inset: 0;
    display: flex; flex-direction: column; align-items: center; justify-content: center; gap: 18px;
  }
  .back-mark__circle {
    width: 150px; height: 150px; border-radius: 50%;
    border: 3px solid var(--silver);
  }
  .back-mark__name {
    font-family: "Cormorant Garamond", serif; font-weight: 600;
    font-size: 22px; letter-spacing: 1px; color: var(--silver);
  }
</style>
</head>
<body>
<main class="canvas">
  <section class="card card--front">
    <div class="portrait" role="img" aria-label="Full-length portrait photo of Marisol Pennington in a black dress, arms crossed"></div>

    <div class="brand-mark">
      <span class="brand-mark__circle"></span>
      <span class="brand-mark__name">Marisol Pennington</span>
    </div>

    <h1 class="name"><span class="name__first">Marisol</span> <span class="name__last">Pennington</span></h1>
    <p class="tagline">Live your life on purpose, no excuses</p>

    <ul class="contact">
      <li>
        <svg viewBox="0 0 24 24" aria-hidden="true"><path d="M6.6 10.8a15.1 15.1 0 0 0 6.6 6.6l2.2-2.2a1 1 0 0 1 1-.25 11.4 11.4 0 0 0 3.6.57 1 1 0 0 1 1 1V20a1 1 0 0 1-1 1A17 17 0 0 1 3 4a1 1 0 0 1 1-1h3.5a1 1 0 0 1 1 1c0 1.25.2 2.45.57 3.6a1 1 0 0 1-.25 1z"/></svg>
        555-214-7396
      </li>
      <li>
        <svg viewBox="0 0 24 24" aria-hidden="true"><path d="M2 5h20v14H2z M3 6l9 7 9-7" fill="var(--gold)"/><path d="M3 6.5l9 6.5 9-6.5" fill="none" stroke="#0b0b0b" stroke-width="1.6"/></svg>
        Www.MarisolPennington.example
      </li>
    </ul>

    <p class="roles">Author | Speaker | Wealth architect</p>
  </section>

  <section class="card card--back">
    <div class="back-mark">
      <span class="back-mark__circle"></span>
      <span class="back-mark__name">Marisol Pennington</span>
    </div>
  </section>
</main>
</body>
</html>
```